Email Banner (LumenBriefs)

We require an email banner for our email promotions sent to prospect clients. The banner needs to contain the wording LumenBriefs and use the same colour scheme as the logos attached.

This is for B2B professional's so needs to look like a place you would come to read technology articles.

```html
<!DOCTYPE html>
<html lang="en">
<head>
<meta charset="utf-8">
<title>LumenBriefs Email Banners</title>
<link rel="stylesheet" href="https://fonts.googleapis.com/css2?family=Outfit:wght@500;600;700&family=Work+Sans:wght@500;600&display=swap">
<style>
  :root {
    --navy: #0b1628;
    --ink: #0d1b2e;
    --white: #ffffff;
    --bar-grey: #d9d9d9;
    --accent-blue: #1a8fd0;
    --accent-green: #5cbf5a;
    --divider-light: #9aa3ad;
    --shadow: rgba(0, 0, 0, 0.55);
  }
  * { margin: 0; padding: 0; box-sizing: border-box; }
  html, body {
    width: 1200px; height: 960px; overflow: hidden;
    background: var(--white);
  }
  .canvas { position: relative; width: 1200px; height: 960px; }

  .banner {
    position: absolute; width: 982px; height: 246px; overflow: hidden;
    box-shadow: 9px 9px 5px var(--shadow);
    font-family: "Outfit", sans-serif;
  }
  .banner--light { left: 116px; top: 106px; background: var(--white); color: var(--ink); box-shadow: 9px 9px 5px var(--shadow), 0 0 0 1px #eeeeee; }
  .banner--dark { left: 119px; top: 386px; background: var(--navy); color: var(--white); }

  .bars { position: absolute; left: 0; top: 0; width: 982px; height: 246px; }

  .brand { position: absolute; display: flex; align-items: center; gap: 14px; }
  .brand__mark { width: 38px; height: 38px; background: var(--accent-green); }
  .brand__name { font-family: "Outfit", sans-serif; font-weight: 500; font-size: 58px; letter-spacing: -0.5px; line-height: 1; }
  .banner--light .brand { left: 64px; top: 45px; }
  .banner--light .brand__name { color: var(--ink); }
  .banner--dark .brand { left: 414px; top: 50px; }
  .banner--dark .brand__name { color: var(--white); font-size: 60px; }

  .info { position: absolute; }
  .info__title { font-family: "Outfit", sans-serif; font-weight: 700; font-size: 22px; letter-spacing: 0.2px; line-height: 1; }
  .info__text { font-family: "Work Sans", sans-serif; font-weight: 600; line-height: 1.22; }
  .banner--light .info { right: 28px; top: 46px; width: 382px; text-align: right; }
  .banner--light .info__text { font-size: 14px; text-align: justify; text-align-last: left; margin-top: 7px; }
  .banner--dark .info { left: 24px; top: 38px; width: 274px; }
  .banner--dark .info__title { font-size: 21px; }
  .banner--dark .info__text { font-size: 10.4px; text-align: justify; margin-top: 10px; line-height: 1.2; }

  .contact { position: absolute; display: flex; flex-direction: column; align-items: center; }
  .banner--light .contact { right: 20px; top: 154px; }
  .banner--dark .contact { left: 50px; top: 150px; }
  .contact__row { display: flex; align-items: stretch; }
  .contact__item {
    display: flex; flex-direction: column; align-items: center; gap: 3px;
    padding: 0 10px; font-weight: 600; font-size: 15px; line-height: 1;
  }
  .contact__item + .contact__item { border-left: 1px solid var(--divider-light); }
  .contact__icon { width: 16px; height: 16px; }
  .social { display: flex; gap: 4px; margin-top: 11px; }
  .social__dot { width: 13px; height: 13px; border-radius: 3px; background: var(--accent-blue); }
  .handle { font-weight: 600; font-size: 15px; margin-top: 4px; line-height: 1; }
</style>
</head>
<body>
<div class="canvas">

  <section class="banner banner--light">
    <svg class="bars" viewBox="0 0 982 246" aria-hidden="true">
      <g fill="var(--bar-grey)">
        <rect x="10" y="180" width="9.6" height="66"/><rect x="27" y="170" width="9.6" height="76"/>
        <rect x="44" y="184" width="9.6" height="62"/><rect x="61" y="190" width="9.6" height="56"/>
        <rect x="78" y="178" width="9.6" height="68"/><rect x="95" y="194" width="9.6" height="52"/>
        <rect x="112" y="168" width="9.6" height="78"/><rect x="129" y="206" width="9.6" height="40"/>
        <rect x="146" y="192" width="9.6" height="54"/><rect x="163" y="182" width="9.6" height="64"/>
        <rect x="180" y="174" width="9.6" height="72"/><rect x="197" y="186" width="9.6" height="60"/>
        <rect x="214" y="166" width="9.6" height="80"/><rect x="231" y="188" width="9.6" height="58"/>
        <rect x="248" y="196" width="9.6" height="50"/><rect x="265" y="190" width="9.6" height="56"/>
        <rect x="282" y="184" width="9.6" height="62"/><rect x="299" y="166" width="9.6" height="80"/>
        <rect x="316" y="176" width="9.6" height="70"/><rect x="333" y="188" width="9.6" height="58"/>
        <rect x="350" y="184" width="9.6" height="62"/><rect x="367" y="196" width="9.6" height="50"/>
        <rect x="384" y="180" width="9.6" height="66"/><rect x="401" y="174" width="9.6" height="72"/>
        <rect x="418" y="188" width="9.6" height="58"/><rect x="435" y="194" width="9.6" height="52"/>
        <rect x="452" y="186" width="9.6" height="60"/><rect x="469" y="202" width="9.6" height="44"/>
        <rect x="486" y="190" width="9.6" height="56"/><rect x="503" y="184" width="9.6" height="62"/>
        <rect x="520" y="198" width="9.6" height="48"/><rect x="537" y="204" width="9.6" height="42"/>
        <rect x="554" y="192" width="9.6" height="54"/><rect x="571" y="176" width="9.6" height="70"/>
        <rect x="588" y="186" width="9.6" height="60"/><rect x="605" y="170" width="9.6" height="76"/>
        <rect x="622" y="198" width="9.6" height="48"/><rect x="639" y="188" width="9.6" height="58"/>
        <rect x="656" y="178" width="9.6" height="68"/><rect x="673" y="190" width="9.6" height="56"/>
        <rect x="690" y="194" width="9.6" height="52"/><rect x="707" y="186" width="9.6" height="60"/>
        <rect x="724" y="198" width="9.6" height="48"/><rect x="741" y="190" width="9.6" height="56"/>
      </g>
    </svg>

    <div class="brand">
      <span class="brand__mark"></span>
      <span class="brand__name">LumenBriefs.io</span>
    </div>

    <div class="info">
      <h2 class="info__title">BUSINESS INFORMATION</h2>
      <p class="info__text">Lorem ipsum dolor sit amet, consectetuer adipiscing elit, sed diam nonummy nibh euismod tincidunt ut laoreet dolore magna aliquam erat volutpat. Ut wisi</p>
    </div>

    <div class="contact">
      <div class="contact__row">
        <div class="contact__item">
          <svg class="contact__icon" viewBox="0 0 16 16" fill="none" stroke="var(--accent-blue)" stroke-width="1.4" stroke-linejoin="round"><path d="M3 2h3l1.2 3-1.7 1.2a8 8 0 0 0 4.3 4.3L11 8.8l3 1.2v3a1 1 0 0 1-1 1A11 11 0 0 1 2 3a1 1 0 0 1 1-1z"/></svg>
          <span>Phone</span>
        </div>
        <div class="contact__item">
          <svg class="contact__icon" viewBox="0 0 16 16" fill="none" stroke="var(--accent-blue)" stroke-width="1.4"><rect x="1.5" y="3.5" width="13" height="9"/><path d="M1.5 3.5 8 9l6.5-5.5"/></svg>
          <span>Email</span>
        </div>
        <div class="contact__item">
          <svg class="contact__icon" viewBox="0 0 16 16" fill="none" stroke="var(--accent-blue)" stroke-width="1.3"><circle cx="8" cy="8" r="6.2"/><ellipse cx="8" cy="8" rx="2.8" ry="6.2"/><path d="M1.8 8h12.4M2.8 5h10.4M2.8 11h10.4"/></svg>
          <span>Website</span>
        </div>
      </div>
      <div class="social"><span class="social__dot"></span><span class="social__dot"></span><span class="social__dot"></span></div>
      <div class="handle">@lumenbriefs</div>
    </div>
  </section>

  <section class="banner banner--dark">
    <svg class="bars" viewBox="0 0 982 246" aria-hidden="true">
      <defs>
        <linearGradient id="barGradient" gradientUnits="userSpaceOnUse" x1="0" y1="146" x2="0" y2="246">
          <stop offset="0" stop-color="var(--accent-green)"/>
          <stop offset="1" stop-color="var(--accent-blue)"/>
        </linearGradient>
      </defs>
      <g fill="url(#barGradient)">
        <rect x="307" y="162" width="10" height="84"/><rect x="324" y="154" width="10" height="92"/>
        <rect x="341" y="172" width="10" height="74"/><rect x="358" y="166" width="10" height="80"/>
        <rect x="375" y="160" width="10" height="86"/><rect x="392" y="170" width="10" height="76"/>
        <rect x="409" y="156" width="10" height="90"/><rect x="426" y="152" width="10" height="94"/>
        <rect x="443" y="162" width="10" height="84"/><rect x="460" y="146" width="10" height="100"/>
        <rect x="477" y="172" width="10" height="74"/><rect x="494" y="184" width="10" height="62"/>
        <rect x="511" y="176" width="10" height="70"/><rect x="528" y="170" width="10" height="76"/>
        <rect x="545" y="152" width="10" height="94"/><rect x="562" y="164" width="10" height="82"/>
        <rect x="579" y="172" width="10" height="74"/><rect x="596" y="158" width="10" height="88"/>
        <rect x="613" y="176" width="10" height="70"/><rect x="630" y="178" width="10" height="68"/>
        <rect x="647" y="164" width="10" height="82"/><rect x="664" y="188" width="10" height="58"/>
        <rect x="681" y="180" width="10" height="66"/><rect x="698" y="172" width="10" height="74"/>
        <rect x="715" y="152" width="10" height="94"/><rect x="732" y="184" width="10" height="62"/>
        <rect x="749" y="172" width="10" height="74"/><rect x="766" y="164" width="10" height="82"/>
        <rect x="783" y="182" width="10" height="64"/><rect x="800" y="174" width="10" height="72"/>
        <rect x="817" y="160" width="10" height="86"/><rect x="834" y="178" width="10" height="68"/>
        <rect x="851" y="186" width="10" height="60"/><rect x="868" y="170" width="10" height="76"/>
        <rect x="885" y="158" width="10" height="88"/><rect x="902" y="176" width="10" height="70"/>
        <rect x="919" y="152" width="10" height="94"/><rect x="936" y="188" width="10" height="58"/>
        <rect x="953" y="170" width="10" height="76"/><rect x="970" y="182" width="10" height="64"/>
      </g>
    </svg>

    <div class="info">
      <h2 class="info__title">BUSINESS INFORMATION</h2>
      <p class="info__text">Lorem ipsum dolor sit amet, consectetuer adipiscing elit, sed diam nonummy nibh euismod tincidunt ut laoreet dolore magna aliquam erat volutpat. Ut wisi enim ad minimdolore magna aliquam erat volutpat</p>
    </div>

    <div class="contact">
      <div class="contact__row">
        <div class="contact__item">
          <svg class="contact__icon" viewBox="0 0 16 16" fill="none" stroke="var(--accent-blue)" stroke-width="1.4" stroke-linejoin="round"><path d="M3 2h3l1.2 3-1.7 1.2a8 8 0 0 0 4.3 4.3L11 8.8l3 1.2v3a1 1 0 0 1-1 1A11 11 0 0 1 2 3a1 1 0 0 1 1-1z"/></svg>
          <span>Phone</span>
        </div>
        <div class="contact__item">
          <svg class="contact__icon" viewBox="0 0 16 16" fill="none" stroke="var(--accent-blue)" stroke-width="1.4"><rect x="1.5" y="3.5" width="13" height="9"/><path d="M1.5 3.5 8 9l6.5-5.5"/></svg>
          <span>Email</span>
        </div>
        <div class="contact__item">
          <svg class="contact__icon" viewBox="0 0 16 16" fill="none" stroke="var(--accent-blue)" stroke-width="1.3"><circle cx="8" cy="8" r="6.2"/><ellipse cx="8" cy="8" rx="2.8" ry="6.2"/><path d="M1.8 8h12.4M2.8 5h10.4M2.8 11h10.4"/></svg>
          <span>Website</span>
        </div>
      </div>
      <div class="social"><span class="social__dot"></span><span class="social__dot"></span><span class="social__dot"></span></div>
      <div class="handle">@lumenbriefs</div>
    </div>

    <div class="brand">
      <span class="brand__mark"></span>
      <span class="brand__name">LumenBriefs.io</span>
    </div>
  </section>

</div>
</body>
</html>
```